Digital Menu Board for Restaurant

I want a digital menu board for our new restaurant. I have provided the sample of what I kind of want.
This is to be on a 55 inch tv so it needs to be the correct aspect ratio of 4:5

Font styles to use
Serif
Sans Serif

Colors
f59296
f04a50
ec1f27
ffffff
fffef7
fbed22
ffc214
0592cd
e5519f

Requirements
Must have
• fun, maybe something moving? bright colors on a darker background so it's easy to read or dark font on a light background.

```html
<!DOCTYPE html>
<html lang="en">
<head>
<meta charset="utf-8">
<title>Sandy Coves – Menu Board</title>
<link rel="stylesheet" href="https://fonts.googleapis.com/css2?family=Comfortaa:wght@600&family=Lobster&family=Kaushan+Script&family=Yanone+Kaffeesatz:wght@400;500&family=Source+Sans+3:wght@400;600&display=swap">
<style>
  :root {
    --board-bg: #2e2933;
    --blue: #1fa3db;
    --orange: #f0622a;
    --yellow: #ffc214;
    --green: #7dc242;
    --white: #fffef7;
  }
  * { box-sizing: border-box; margin: 0; padding: 0; }
  html, body { width: 1200px; height: 757px; overflow: hidden; background: var(--board-bg); }
  .board {
    position: relative; width: 1200px; height: 757px;
    background: var(--board-bg); color: var(--white);
    font-family: "Source Sans 3", sans-serif;
  }
  .combo {
    position: absolute; left: 60px; top: 36px;
    font-family: "Comfortaa", sans-serif; font-weight: 600;
    color: var(--blue); font-size: 44px; line-height: 50px;
    text-transform: uppercase; letter-spacing: 1px;
  }
  .brand {
    position: absolute; left: 930px; top: 120px; width: 240px;
    font-family: "Source Sans 3", sans-serif; font-weight: 600;
    color: var(--orange); font-size: 40px; line-height: 1;
  }
  .section-title {
    font-family: "Lobster", serif; color: var(--orange);
    font-size: 38px; line-height: 1; margin-bottom: 8px;
  }
  .section-title.small { font-size: 32px; }
  .section-title.green {
    font-family: "Kaushan Script", cursive; color: var(--green);
    font-size: 26px; margin-bottom: 6px;
  }
  .item-name {
    font-family: "Yanone Kaffeesatz", sans-serif; font-weight: 500;
    color: var(--blue); font-size: 25px; line-height: 1.05;
  }
  .item-desc {
    color: var(--yellow); font-size: 15px; line-height: 18px;
    margin-bottom: 8px;
  }
  .col-buns { position: absolute; left: 60px; top: 252px; width: 340px; }
  .col-shore { position: absolute; left: 540px; top: 262px; width: 290px; }
  .col-shore .item-name { font-size: 22px; }
  .col-shore .item-desc { font-size: 13px; line-height: 16px; margin-bottom: 7px; }
  .kids { margin-top: 20px; }
  .kids .section-title.green { font-size: 30px; }
  .kids-list { color: var(--white); font-size: 16px; line-height: 21px; }
  .col-extras { position: absolute; left: 930px; top: 300px; width: 240px; }
  .extras-text {
    font-family: "Yanone Kaffeesatz", sans-serif; font-weight: 400;
    color: var(--white); font-size: 16px; line-height: 19px; margin-bottom: 14px;
  }
  .sides { display: grid; grid-template-columns: 1fr 1fr; column-gap: 8px; list-style: none; }
  .sides li::before { content: "•"; color: var(--green); margin-right: 5px; }
</style>
</head>
<body>
<main class="board">
  <div class="combo">
    <p>Combp Up!</p>
    <p>Add 1 side and drink</p>
    <p>Add 1 side and shake</p>
    <p>Additional sides</p>
  </div>

  <div class="brand">Sandy Coves</div>

  <section class="col-buns">
    <h2 class="section-title">Between Buns</h2>
    <h3 class="item-name">1st Point Pulled Pork</h3>
    <p class="item-desc">Pulled Pork, Rick's Sassy BBQ Sauce, Chopped Bacon, Pepperjack Cheese, and Fried Jalapeno Peppers on a Ciabatta Bun</p>
    <h3 class="item-name">2nd Point Pulled Pork</h3>
    <p class="item-desc">Pulled Pork, Rick's Sweet Respberry BBQ Sauce, and Coleslaw on a Ciabatta Bun</p>
    <h3 class="item-name">Spinikea Point Burger</h3>
    <p class="item-desc">Smokehouse 1/2 Pound Burger, Crumbled Bacon, Rick's Sassy BBQ Sauce, Cheese, and Onion Rings on a Toasted Brioche Bun</p>
    <h3 class="item-name">The Rock Burger</h3>
    <p class="item-desc">Two Smokehouse 1/2 Pound Patties, Cheese, Lettuce, Tomato, Onion, Pickles, on Toasted Brioche Bun</p>
    <h3 class="item-name">Rainbow Cove Sandwich</h3>
    <p class="item-desc">Chicken Salad - Smoked Chicken, Celery, and Onion Mixed with our BBQ Mayo and Topped with Seasoned Tomato on a Hoagie Roll.</p>
  </section>

  <section class="col-shore">
    <h2 class="section-title small">Green Shore</h2>
    <h3 class="item-name">North Beach Salad</h3>
    <p class="item-desc">Pulled pord and Black Beans on a Bed of Romaine, Tomato and Onion with Sweet and Sour Respberry Pineapple Sauce.</p>
    <h3 class="item-name">West Side Salad</h3>
    <p class="item-desc">BBQ Pulled Pork, Crumbled Bacon, Candied Walnuts, Feta Cheese, Red Onion, Spinach and Lettuce with Ranch Dressing or Raspberry Vinaigrette</p>
    <h3 class="item-name">Ease Side Salad</h3>
    <p class="item-desc">Spinach and Lettuce, Chopped Apples, Candied Walnuts, Onion, Feta Cheese with Rick's Respberry Vinaigrette<br>Add Chicken:</p>
    <div class="kids">
      <h2 class="section-title green">Seashell Finders(Kids)</h2>
      <p class="kids-list">Little Cheeseburger Pulled pork sandwich<br>Mini Corn Dogs Chicken salad sandwich<br>Fries/Onion Rings</p>
    </div>
  </section>

  <section class="col-extras">
    <h2 class="section-title green">Drinks</h2>
    <p class="extras-text">Fizz Cola, Diet Fizz, Red Cola, Diet Red, Peak Soda, Diet Peak, Lemonade, Lime Pop, Dr Spark</p>
    <h2 class="section-title green">Sides</h2>
    <ul class="sides extras-text">
      <li>Seasoned Fries</li><li>Sweet Coleslaw</li>
      <li>Onion Rings</li><li>Macaroni Salad</li>
      <li>Sweet Cornbread</li><li>Side Salad</li>
    </ul>
    <h2 class="section-title green">Shakes</h2>
    <p class="extras-text">Rick's Signature Raspberry Jammin Shake<br>Raspberry Hazelnut Bobm Shake<br>Raspberry Beachin' Shake (Pina Colada)<br>Raspberry Browine Shake<br>Caramel Shake<br>Chocolate Shake</p>
  </section>
</main>
</body>
</html>
```